Web App Dashboard Design for a Smart Home

We are a company that gives consultancy and installation services for custom smart home designs to household owners in ON, Canada. For our web application, we are in need of a dashboard design which will display multiple rooms that could be present in a home. This should be a flexible design as the number of rooms where smart devices installed will vary from house to house. We would like to see the name of the rooms and several icons that represent different monitored objects in each room like temperature, light on/off, sound/music on/off, humidity, illuminance, noise level, air quality, for bathrooms and kitchens wet/dry conditions, windows/doors open, curtains open/closed etc. The web application will collect the latest status data from all related sensors and it will be publishing the latest status for each room into this dashboard. Backend of the dashboards should contain nice modern looking houses and it would be good if there are multiple versions of the background pictures that rotate.

Target Market(s)

Mid-Market range house holders who want to increase their comfort and safety with smart home implementations

Industry/Entity Type

Small Business

Number of Pages Required

1 page

Colors
0455a3
3277b5
85acd3
86cae7
fbf289
cadf82
acd037
9bcb3c
faa54b

Requirements
Must have
• - A Flexible Dashboard Design which can hold many rooms but still look sharp even with only 1/2 rooms as well.
• - An smart home icon library that will show the monitored value like temperature, lights on/off, door/window open/close etc.

```html
<!DOCTYPE html>
<html lang="en">
<head>
<meta charset="utf-8">
<title>Smart Home Dashboard</title>
<link href="https://fonts.googleapis.com/css2?family=Montserrat:wght@500;700&family=Roboto:wght@400;500&display=swap" rel="stylesheet">
<style>
  :root{
    --sidebar:#2f5fd3;
    --canvas:#e9e9e9;
    --card:#ffffff;
    --title:#0455a3;
    --ink:#1f1f1f;
    --entrance:#f9a825;
    --living:#5e35b1;
    --bath:#388e3c;
    --bedroom:#ff6d00;
    --camera:#f50057;
    --toggle-on:#4cd964;
    --toggle-off:#c8c8c8;
  }
  *{box-sizing:border-box;margin:0;padding:0}
  html,body{width:1200px;height:886px;overflow:hidden;background:var(--canvas)}
  body{font-family:"Roboto",sans-serif;color:var(--ink);display:flex}
  .sidebar{width:104px;height:886px;background:var(--sidebar);display:flex;flex-direction:column;align-items:center;padding-top:36px}
  .nav-item{display:flex;flex-direction:column;align-items:center;color:#fff;font-size:12.5px;margin-bottom:28px}
  .nav-item svg{width:30px;height:30px;margin-bottom:3px;fill:#fff}
  .nav-item.logout{margin-top:auto;margin-bottom:60px}
  .main{flex:1;padding:40px 0 0 105px}
  .page-title{font-family:"Montserrat",sans-serif;font-weight:700;font-size:25px;color:var(--title);line-height:1.1}
  .page-sub{font-family:"Montserrat",sans-serif;font-weight:500;font-size:13px;margin-top:1px}
  .grid{display:grid;grid-template-columns:290px 290px 290px;gap:15px 13px;margin-top:27px;align-items:start}
  .card{background:var(--card);border-radius:3px;box-shadow:0 1px 3px rgba(0,0,0,.12);overflow:hidden}
  .card-head{height:40px;display:flex;align-items:center;padding:0 11px;color:#fff;font-weight:500;font-size:12px}
  .entrance .card-head{background:var(--entrance)}
  .living .card-head{background:var(--living)}
  .bath .card-head{background:var(--bath)}
  .bedroom .card-head{background:var(--bedroom)}
  .camera .card-head{background:var(--camera)}
  .room{height:234px}
  .bedroom{height:335px}
  .stats{display:flex;justify-content:center;gap:30px;padding-top:20px;height:92px}
  .entrance .stats{justify-content:space-around;gap:0;padding-left:12px;padding-right:12px}
  .stat{display:flex;flex-direction:column;align-items:center;width:60px;text-align:center}
  .stat svg{width:24px;height:28px;margin-bottom:4px}
  .stat .val{font-size:14px}
  .stat .val.small{font-size:11px;line-height:1.15}
  .devices{list-style:none;padding:0 18px}
  .device{display:flex;align-items:center;height:37px}
  .device svg{width:24px;height:26px;margin-right:20px;flex:none}
  .device .name{flex:1;font-size:13px}
  .toggle{width:24px;height:12px;border-radius:6px;background:var(--toggle-off);position:relative}
  .toggle::after{content:"";position:absolute;top:-2px;left:-1px;width:15px;height:15px;border-radius:50%;background:#fff;box-shadow:0 1px 2px rgba(0,0,0,.35)}
  .toggle.on{background:var(--toggle-on)}
  .toggle.on::after{left:10px}
  .camera{grid-column:span 2;height:456px}
  .camera-feed{margin:17px 18px 0;height:382px;background:linear-gradient(180deg,#dfe6ea 0%,#cfd6da 28%,#8a6c5c 42%,#6d6a6a 60%,#5b6a8e 72%,#7c8a55 100%)}
  svg.ico{fill:none;stroke:#111;stroke-width:1.4;stroke-linecap:round;stroke-linejoin:round}
</style>
</head>
<body>
  <nav class="sidebar">
    <div class="nav-item"><svg viewBox="0 0 24 24"><path d="M12 3 1 12h3v9h6v-6h4v6h6v-9h3z"/></svg>Dashboard</div>
    <div class="nav-item"><svg viewBox="0 0 24 24"><rect x="3" y="14" width="3" height="8"/><rect x="8" y="11" width="3" height="11"/><rect x="13" y="15" width="3" height="7"/><rect x="18" y="9" width="3" height="13"/><path d="M2 10l6-5 5 4 8-7" stroke="#fff" stroke-width="2" fill="none"/></svg>Usage</div>
    <div class="nav-item"><svg viewBox="0 0 24 24"><path d="M12 2a2 2 0 0 1 2 2v1a7 7 0 0 1 5 7v5l2 2H3l2-2v-5a7 7 0 0 1 5-7V4a2 2 0 0 1 2-2zm-2 19h4a2 2 0 0 1-4 0z"/></svg>Notifications</div>
    <div class="nav-item"><svg viewBox="0 0 24 24"><path d="M10 2h4l.6 3 2.3 1 2.6-1.7 2.8 2.8-1.7 2.6 1 2.3 3 .6v4l-3 .6-1 2.3 1.7 2.6-2.8 2.8-2.6-1.7-2.3 1-.6 3h-4l-.6-3-2.3-1-2.6 1.7-2.8-2.8L4.5 17l-1-2.3-3-.6v-4l3-.6 1-2.3L2.8 4.6l2.8-2.8L8.2 3.5l2.3-1zM12 8a4 4 0 1 0 0 8 4 4 0 0 0 0-8z" transform="scale(.92) translate(1 1)"/></svg>Configuration</div>
    <div class="nav-item logout"><svg viewBox="0 0 24 24"><path d="M9 4H5a2 2 0 0 0-2 2v12a2 2 0 0 0 2 2h4" stroke="#fff" stroke-width="2.6" fill="none"/><path d="M10 10h6V6l7 6-7 6v-4h-6z"/></svg>Logout</div>
  </nav>

  <main class="main">
    <h1 class="page-title">Dashboard</h1>
    <p class="page-sub">Here you can control every aspect of your house, for each room individually</p>

    <section class="grid">
      <article class="card room entrance">
        <header class="card-head">Main entrance</header>
        <div class="stats">
          <div class="stat"><svg class="ico" viewBox="0 0 24 28"><path d="M10 3a2 2 0 0 1 4 0v14a5 5 0 1 1-4 0z"/><circle cx="12" cy="21" r="2" fill="#111"/><path d="M12 8v11"/></svg><span class="val">58°F</span></div>
          <div class="stat"><svg class="ico" viewBox="0 0 28 28"><path d="M3 11h4l8-5v16l-8-5H3z"/><path d="M19 9l5-3M19 14h6M19 19l5 3M19 11.5l5-1.5M19 16.5l5 1.5"/></svg><span class="val small">High noise<br>levels</span></div>
          <div class="stat"><svg class="ico" viewBox="0 0 24 28"><path d="M12 3v22M3 8l18 12M21 8 3 20M9 4l3 3 3-3M9 24l3-3 3 3M3 12l4-2-1-4M21 12l-4-2 1-4M3 16l4 2-1 4M21 16l-4 2 1 4"/></svg><span class="val small">Cold</span></div>
        </div>
        <ul class="devices">
          <li class="device"><svg class="ico" viewBox="0 0 24 26"><path d="M12 1v5M10 6h4M4 15a8 8 0 0 1 16 0z"/><path d="M9 18a3 3 0 0 0 6 0M4 21l-2 2M20 21l2 2M12 22v3"/></svg><span class="name">Celing light</span><span class="toggle on"></span></li>
          <li class="device"><svg class="ico" viewBox="0 0 24 26"><rect x="6" y="2" width="12" height="22"/><path d="M9 2v22"/><circle cx="15" cy="13" r=".8" fill="#111"/></svg><span class="name">Front door</span><span class="toggle"></span></li>
        </ul>
      </article>

      <article class="card room living">
        <header class="card-head">Living room</header>
        <div class="stats">
          <div class="stat"><svg class="ico" viewBox="0 0 24 28"><path d="M10 3a2 2 0 0 1 4 0v14a5 5 0 1 1-4 0z"/><circle cx="12" cy="21" r="2" fill="#111"/><path d="M12 8v11"/></svg><span class="val">75°F</span></div>
          <div class="stat"><svg class="ico" viewBox="0 0 24 28"><path d="M12 4c4 6 7 9 7 13a7 7 0 0 1-14 0c0-4 3-7 7-13z"/><path d="M9 17a3 3 0 0 0 3 3"/></svg><span class="val small">23%</span></div>
        </div>
        <ul class="devices">
          <li class="device"><svg class="ico" viewBox="0 0 24 26"><path d="M12 1v5M10 6h4M4 15a8 8 0 0 1 16 0z"/><path d="M9 18a3 3 0 0 0 6 0M4 21l-2 2M20 21l2 2M12 22v3"/></svg><span class="name">Celing light 1</span><span class="toggle"></span></li>
          <li class="device"><svg class="ico" viewBox="0 0 24 26"><path d="M12 1v5M10 6h4M4 15a8 8 0 0 1 16 0z"/><path d="M9 18a3 3 0 0 0 6 0M4 21l-2 2M20 21l2 2M12 22v3"/></svg><span class="name">Celing light 2</span><span class="toggle"></span></li>
        </ul>
      </article>

      <article class="card room bath">
        <header class="card-head">Guest bathroom</header>
        <div class="stats">
          <div class="stat"><svg class="ico" viewBox="0 0 24 28"><path d="M10 3a2 2 0 0 1 4 0v14a5 5 0 1 1-4 0z"/><circle cx="12" cy="21" r="2" fill="#111"/><path d="M12 8v11"/></svg><span class="val">43°F</span></div>
          <div class="stat"><svg class="ico" viewBox="0 0 24 28"><path d="M12 4c4 6 7 9 7 13a7 7 0 0 1-14 0c0-4 3-7 7-13z"/><path d="M9 17a3 3 0 0 0 3 3"/></svg><span class="val small">70%</span></div>
        </div>
        <ul class="devices">
          <li class="device"><svg class="ico" viewBox="0 0 24 26"><path d="M12 1v5M10 6h4M4 15a8 8 0 0 1 16 0z"/><path d="M9 18a3 3 0 0 0 6 0M4 21l-2 2M20 21l2 2M12 22v3"/></svg><span class="name">Celing light</span><span class="toggle on"></span></li>
          <li class="device"><svg class="ico" viewBox="0 0 24 26"><path d="M12 7a5 5 0 0 0-3 9v3h6v-3a5 5 0 0 0-3-9zM10 22h4M12 1v3M4 5l2 2M20 5l-2 2M2 12h2M20 12h2"/></svg><span class="name">Mirror light</span><span class="toggle on"></span></li>
        </ul>
      </article>

      <article class="card bedroom">
        <header class="card-head">Master bedroom</header>
        <div class="stats">
          <div class="stat"><svg class="ico" viewBox="0 0 24 28"><path d="M10 3a2 2 0 0 1 4 0v14a5 5 0 1 1-4 0z"/><circle cx="12" cy="21" r="2" fill="#111"/><path d="M12 8v11"/></svg><span class="val">75°F</span></div>
          <div class="stat"><svg class="ico" viewBox="0 0 24 28"><path d="M12 4c4 6 7 9 7 13a7 7 0 0 1-14 0c0-4 3-7 7-13z"/><path d="M9 17a3 3 0 0 0 3 3"/></svg><span class="val small">23%</span></div>
        </div>
        <ul class="devices">
          <li class="device"><svg class="ico" viewBox="0 0 24 26"><path d="M12 1v5M10 6h4M4 15a8 8 0 0 1 16 0z"/><path d="M9 18a3 3 0 0 0 6 0M4 21l-2 2M20 21l2 2M12 22v3"/></svg><span class="name">Celing light</span><span class="toggle on"></span></li>
          <li class="device"><svg class="ico" viewBox="0 0 24 26"><path d="M8 2h8l2 9H6zM12 11v9M7 20h10v4H7z"/></svg><span class="name">Left night lamp</span><span class="toggle"></span></li>
          <li class="device"><svg class="ico" viewBox="0 0 24 26"><path d="M8 2h8l2 9H6zM12 11v9M7 20h10v4H7z"/></svg><span class="name">Left night lamp</span><span class="toggle"></span></li>
          <li class="device"><svg class="ico" viewBox="0 0 24 26"><rect x="1" y="6" width="22" height="9"/><path d="M4 12h16M7 18l-1 3M12 18v3M17 18l1 3"/></svg><span class="name">A/C</span><span class="toggle"></span></li>
          <li class="device"><svg class="ico" viewBox="0 0 24 26"><rect x="1" y="4" width="22" height="9" fill="#111"/><path d="M12 13v7"/><circle cx="12" cy="21" r="1"/></svg><span class="name">Blinds</span><span class="toggle"></span></li>
        </ul>
      </article>

      <article class="card camera">
        <header class="card-head">Driveway Camera</header>
        <div class="camera-feed" role="img" aria-label="Live driveway camera view: a parked car on the drive with brick houses and a lawn under a pale sky"></div>
      </article>
    </section>
  </main>
</body>
</html>
```